Business card design needed

After a business card which portrays the same precision tig welding and performance fabrications we offer customers. Catering mainly for the automotive market, but process work for marine, industrial & hospitality work is definitely welcome.

We provide the same level quality, care and workmanship regardless of how big or small the job is. Quality is the first and foremost for customers looking for the highest standards around along with a customised look not found anywhere else.

Our offering is tailor made for each customer and where needed, a completely individual look

Colours - red, black and white (as per the attached logo)

The design should portray a customised/one-off solution for each customer with a high attention to detail.
Updates

The brief should have included this design is required for a 2 sided card

Industry/Entity Type

Hospitality

Contact Information for Business Card

Blue Anchor Metalworks
3/14 Corwen Hale Avenue
North Wollongong NSW 2500

Ph: 02 4871 3064
Mob: 0412 586 137
Email: blueanchormetalworks@mailhaven.example
Facebook: www.socialpage.example/blueanchormetalworks

Requirements
Must have
• Must have a catchy front side without being cluttered & brief but list off main offerings on the back. For eg
- customised concept & design for each project
- 2D & 3D modelling & machining
- catering for single or mass prodcued items

```html
<!DOCTYPE html>
<html lang="en">
<head>
<meta charset="utf-8">
<title>Blue Anchor Metalworks – Business Card</title>
<link rel="stylesheet" href="https://fonts.googleapis.com/css2?family=Exo+2:wght@400;500;700;800&display=swap">
<style>
  :root {
    --stage-top: #1c1c1e;
    --stage-bottom: #d9d9db;
    --card-dark: #121214;
    --card-mid: #2a2a2d;
    --accent-red: #d0202e;
    --text-white: #f4f4f4;
    --text-soft: #e2e2e2;
  }
  * { box-sizing: border-box; margin: 0; padding: 0; }
  html, body {
    width: 1200px;
    height: 861px;
    overflow: hidden;
  }
  body {
    background: linear-gradient(180deg, var(--stage-top) 0%, #3a3a3d 45%, var(--stage-bottom) 100%);
    font-family: "Exo 2", sans-serif;
    color: var(--text-white);
    position: relative;
  }
  .card {
    position: absolute;
    top: 270px;
    width: 520px;
    height: 318px;
    background: linear-gradient(135deg, var(--card-mid) 0%, var(--card-dark) 60%, #0b0b0c 100%);
    box-shadow: 0 18px 40px rgba(0, 0, 0, 0.55);
    padding: 48px 40px 0 52px;
  }
  .card--back { left: 50px; }
  .card--front { left: 630px; padding-left: 56px; }

  .brand {
    display: flex;
    align-items: center;
    gap: 12px;
    font-weight: 800;
    font-size: 30px;
    letter-spacing: 0.5px;
    color: var(--text-white);
    line-height: 1;
  }
  .brand__dot {
    width: 18px;
    height: 18px;
    border-radius: 50%;
    background: var(--accent-red);
    flex: none;
  }
  .card--back .brand { justify-content: center; padding-right: 20px; }

  .offer__title {
    margin-top: 34px;
    color: var(--accent-red);
    font-weight: 500;
    font-size: 17px;
    letter-spacing: 0.5px;
  }
  .offer__list { list-style: none; margin-top: 6px; }
  .offer__item {
    display: flex;
    align-items: center;
    gap: 8px;
    font-size: 16.5px;
    color: var(--text-soft);
    line-height: 28px;
  }
  .offer__item::before {
    content: "";
    width: 16px;
    height: 2px;
    background: linear-gradient(90deg, transparent, var(--accent-red));
  }
  .offer__item::after {
    content: "";
    order: -1;
  }
  .offer__bullet {
    width: 9px;
    height: 9px;
    border-radius: 50%;
    background: var(--accent-red);
    flex: none;
    margin-left: -6px;
  }

  .contact { list-style: none; margin-top: 40px; }
  .contact__row {
    display: flex;
    align-items: center;
    gap: 10px;
    font-size: 14.5px;
    color: var(--text-soft);
    line-height: 27px;
  }
  .contact__icon {
    width: 20px;
    height: 20px;
    flex: none;
  }
</style>
</head>
<body>

  <section class="card card--back" aria-label="Card back">
    <div class="brand"><span class="brand__dot"></span>Blue Anchor Metalworks</div>
    <h2 class="offer__title">WE OFFER:</h2>
    <ul class="offer__list">
      <li class="offer__item"><span class="offer__bullet"></span>Precision tig welding of all materials</li>
      <li class="offer__item"><span class="offer__bullet"></span>Customised concept &amp; design of each project</li>
      <li class="offer__item"><span class="offer__bullet"></span>2D &amp; 3D modelling &amp; machining</li>
      <li class="offer__item"><span class="offer__bullet"></span>Catering for one-off products to production pieces</li>
      <li class="offer__item"><span class="offer__bullet"></span>Fully equipped fabrication workshop</li>
    </ul>
  </section>

  <section class="card card--front" aria-label="Card front">
    <div class="brand"><span class="brand__dot"></span>Blue Anchor Metalworks</div>
    <ul class="contact">
      <li class="contact__row">
        <svg class="contact__icon" viewBox="0 0 20 20" aria-hidden="true">
          <circle cx="10" cy="10" r="9" fill="none" stroke="var(--accent-red)" stroke-width="1.5"/>
          <path d="M10 4.5a3.5 3.5 0 0 0-3.5 3.5c0 2.6 3.5 6.5 3.5 6.5s3.5-3.9 3.5-6.5A3.5 3.5 0 0 0 10 4.5z" fill="var(--accent-red)"/>
          <circle cx="10" cy="8" r="1.2" fill="var(--card-dark)"/>
        </svg>
        3/14 Corwen Hale Avenue North Wollongong NSW 2500
      </li>
      <li class="contact__row">
        <svg class="contact__icon" viewBox="0 0 20 20" aria-hidden="true">
          <circle cx="10" cy="10" r="9" fill="none" stroke="var(--accent-red)" stroke-width="1.5"/>
          <path d="M6.5 5.5l2 0 1 2.5-1.3 1a6 6 0 0 0 2.8 2.8l1-1.3 2.5 1v2a1 1 0 0 1-1 1A8 8 0 0 1 5.5 6.5a1 1 0 0 1 1-1z" fill="var(--accent-red)"/>
        </svg>
        02 4871 3064
      </li>
      <li class="contact__row">
        <svg class="contact__icon" viewBox="0 0 20 20" aria-hidden="true">
          <circle cx="10" cy="10" r="9" fill="none" stroke="var(--accent-red)" stroke-width="1.5"/>
          <rect x="7" y="4.5" width="6" height="11" rx="1" fill="none" stroke="var(--accent-red)" stroke-width="1.4"/>
          <circle cx="10" cy="13.6" r="0.8" fill="var(--accent-red)"/>
        </svg>
        0412 586 137
      </li>
      <li class="contact__row">
        <svg class="contact__icon" viewBox="0 0 20 20" aria-hidden="true">
          <circle cx="10" cy="10" r="9" fill="none" stroke="var(--accent-red)" stroke-width="1.5"/>
          <rect x="5" y="6.5" width="10" height="7" fill="var(--accent-red)"/>
          <path d="M5 6.5l5 4 5-4" fill="none" stroke="var(--card-dark)" stroke-width="1"/>
        </svg>
        blueanchormetalworks@mailhaven.example
      </li>
      <li class="contact__row">
        <svg class="contact__icon" viewBox="0 0 20 20" aria-hidden="true">
          <circle cx="10" cy="10" r="9" fill="none" stroke="var(--accent-red)" stroke-width="1.5"/>
        </svg>
        www.socialpage.example/blueanchormetalworks
      </li>
    </ul>
  </section>

</body>
</html>
```